SPÄTER FREI!
Zielgruppe
Mein Ebook 'SPÄTER FREI!' soll den Untertitel 'Wie du Depressionen, Süchte und Einsamkeit überwindest und dein Leben veränderst' haben. Genau darum geht es und das soll das auch Cover vermitteln. Der Autor des Buches heißt Olaf Brenner.

```html
<!DOCTYPE html>
<html lang="de">
<head>
<meta charset="utf-8">
<title>Später Frei – Olaf Brenner</title>
<link rel="stylesheet" href="https://fonts.googleapis.com/css2?family=Fredoka:wght@600;700&display=swap">
<style>
  :root {
    --cover-black: #000000;
    --title-blue: #0a8ad6;
    --splash-pink: #e8338f;
    --splash-orange: #f08a2a;
    --splash-yellow: #f4d23a;
    --splash-green: #7fae3c;
    --splash-sky: #4fa6e0;
  }
  html, body {
    margin: 0;
    padding: 0;
    width: 848px;
    height: 1200px;
    overflow: hidden;
    background: var(--cover-black);
  }
  .cover {
    position: relative;
    width: 848px;
    height: 1200px;
    background: var(--cover-black);
    font-family: "Fredoka", "Arial Rounded MT Bold", sans-serif;
    color: var(--title-blue);
    overflow: hidden;
  }
  .cover-figure {
    position: absolute;
    left: 100px;
    top: 258px;
    width: 690px;
    height: 880px;
    border-radius: 50%;
    background:
      radial-gradient(ellipse 28% 22% at 62% 22%, var(--splash-pink) 0%, transparent 100%),
      radial-gradient(ellipse 22% 20% at 50% 38%, var(--splash-yellow) 0%, transparent 100%),
      radial-gradient(ellipse 24% 22% at 44% 34%, var(--splash-orange) 0%, transparent 100%),
      radial-gradient(ellipse 20% 22% at 55% 55%, var(--splash-green) 0%, transparent 100%),
      radial-gradient(ellipse 30% 26% at 32% 72%, var(--splash-sky) 0%, transparent 100%),
      radial-gradient(ellipse 30% 26% at 72% 74%, var(--splash-pink) 0%, transparent 100%);
    opacity: 0.85;
  }
  .cover-title {
    position: absolute;
    top: 62px;
    left: 0;
    width: 100%;
    margin: 0;
    text-align: center;
    font-weight: 700;
    font-size: 112px;
    line-height: 108px;
    letter-spacing: 2px;
  }
  .cover-subtitle {
    position: absolute;
    top: 276px;
    left: 0;
    width: 100%;
    margin: 0;
    text-align: center;
    font-weight: 600;
    font-size: 25px;
    line-height: 42px;
    letter-spacing: 1.6px;
  }
  .cover-author {
    position: absolute;
    top: 1130px;
    left: 0;
    width: 100%;
    margin: 0;
    text-align: center;
    font-weight: 600;
    font-size: 30px;
    letter-spacing: 2px;
  }
</style>
</head>
<body>
  <main class="cover">
    <div class="cover-figure" role="img" aria-label="Illustration: Silhouette einer springenden Tänzerin aus bunten Farbklecksen in Pink, Orange, Gelb, Grün und Blau"></div>
    <h1 class="cover-title">Später<br>Frei</h1>
    <p class="cover-subtitle">Wie du Depressionen, Süchte und Einsamkeit<br>überwindest und dein Leben veränderst</p>
    <p class="cover-author">Olaf Brenner</p>
  </main>
</body>
</html>
```